Tualong business card -we import and distributed Chinese herbal medicine into Australia for prac...

We need a business card for our recently purchased and rebranded company. We are a small family run business - husband and wife team. Our logo is red and black, and we would like the card to be white, with an element of gold in the design (the first cloud in the attached png) which when printed we would like embossed in gold. Our website uses Chinese water colour paintings in the banners (www.tualong.net.au) so a design that is in harmony with this would be ideal.
side one needs to include:

Target Market(s)

potential customers

Industry/Entity Type

Health And Wellness

Contact Information for Business Card

Side 1
logo,
Desmond Parrow Director
Practitioner Support and Education
0491 628 403
desmond@tualong.net.au
218 Kellby St, Kestrel Downs, QLD, 4417

side 2 needs to include:
logo
Rosalind Chetty Director
Orders, Accounts and Despatch
0497 352 810
rosalind@tualong.net.au

Font styles to use
Serif

Colors

Designer to choose colors to be used in the design.

Requirements
Must have
• black, red, gold colours
Nice to have
• we like the font papyrus (mac font)

```html
<!DOCTYPE html>
<html lang="en">
<head>
<meta charset="utf-8">
<title>Tualong Business Cards</title>
<link rel="stylesheet" href="https://fonts.googleapis.com/css2?family=Caveat:wght@400;600&family=Cormorant+Garamond:wght@400;500;600&display=swap">
<style>
  :root {
    --page: #e9ebef;
    --card: #ffffff;
    --ink: #1c1c22;
    --ink-soft: #3a3a44;
    --brand-navy: #1f2747;
    --seal-red: #d3261f;
    --gold: #f1be2a;
    --wash-blue: #a9c8e6;
    --mountain-deep: #34497f;
    --mountain-mid: #6f86b8;
    --mountain-light: #dfe7f1;
  }
  * { box-sizing: border-box; margin: 0; padding: 0; }
  html, body { width: 1200px; height: 1200px; overflow: hidden; }
  body {
    background: var(--page);
    display: flex;
    flex-direction: column;
    align-items: center;
    justify-content: center;
    gap: 40px;
    font-family: "Cormorant Garamond", Georgia, serif;
    color: var(--ink);
  }
  .business-card {
    position: relative;
    width: 860px;
    height: 524px;
    background: var(--card);
    border-radius: 22px;
    overflow: hidden;
    box-shadow: 0 8px 24px rgba(20, 30, 60, 0.15);
  }
  .mountain-wash {
    position: absolute;
    left: 0; right: 0; bottom: 0;
    height: 62%;
    background:
      linear-gradient(160deg, rgba(255,255,255,0) 0%, rgba(255,255,255,0) 46%, var(--mountain-light) 60%, var(--mountain-mid) 76%, var(--mountain-deep) 90%, var(--mountain-light) 100%);
  }
  .brand-lockup {
    position: absolute;
    top: 42px; right: 60px;
    display: flex;
    align-items: center;
    gap: 16px;
  }
  .brand-square {
    width: 40px; height: 56px;
    background: var(--seal-red);
  }
  .brand-name {
    font-family: "Cormorant Garamond", Georgia, serif;
    font-weight: 500;
    font-size: 48px;
    letter-spacing: 0.06em;
    text-transform: uppercase;
    color: var(--brand-navy);
  }
  .cloud-emblem {
    position: absolute;
    top: 130px; right: 110px;
    width: 150px; height: 120px;
    border-radius: 50%;
    background: radial-gradient(circle at 50% 55%, var(--gold) 0 34%, var(--wash-blue) 62%, rgba(169,200,230,0) 72%);
  }
  .contact-block {
    position: absolute;
    left: 60px; top: 180px;
  }
  .person-name {
    font-family: "Caveat", cursive;
    font-weight: 400;
    font-size: 50px;
    line-height: 1;
    color: var(--ink);
  }
  .person-role {
    font-size: 17px;
    font-weight: 500;
    margin-top: 4px;
    color: var(--ink-soft);
  }
  .department {
    margin-top: 26px;
    color: var(--ink-soft);
    line-height: 1.05;
  }
  .department-top { font-size: 21px; }
  .department-bottom { font-size: 28px; letter-spacing: 0.12em; padding-left: 18px; }
  .phone {
    margin-top: 26px;
    font-family: "Caveat", cursive;
    font-weight: 600;
    font-size: 46px;
    line-height: 1;
    color: var(--ink);
  }
  .contact-line {
    font-size: 20px;
    font-weight: 500;
    color: var(--ink);
    line-height: 1.3;
  }
  .contact-line.email { padding-left: 24px; }
  .contact-line.address { padding-left: 44px; }
</style>
</head>
<body>

  <section class="business-card card-orders">
    <div class="mountain-wash" role="img" aria-label="Chinese watercolour painting of misty blue mountains"></div>
    <div class="brand-lockup">
      <div class="brand-square"></div>
      <div class="brand-name">Tualong</div>
    </div>
    <div class="cloud-emblem" role="img" aria-label="Gold auspicious cloud motif on a pale blue watercolour wash"></div>
    <div class="contact-block">
      <h1 class="person-name">Rosalind Chetty</h1>
      <p class="person-role">Director</p>
      <div class="department">
        <p class="department-top">Orders, Accounts</p>
        <p class="department-bottom">&amp; Despatch</p>
      </div>
      <p class="phone">0497 352 810</p>
      <p class="contact-line email">rosalind@tualong.net.au</p>
      <p class="contact-line address">218 Kellby St, Kestrel Downs, QLD, 4417</p>
    </div>
  </section>

  <section class="business-card card-practitioner">
    <div class="mountain-wash" role="img" aria-label="Chinese watercolour painting of misty blue mountains"></div>
    <div class="brand-lockup">
      <div class="brand-square"></div>
      <div class="brand-name">Tualong</div>
    </div>
    <div class="cloud-emblem" role="img" aria-label="Gold auspicious cloud motif on a pale blue watercolour wash"></div>
    <div class="contact-block">
      <h1 class="person-name">Desmond Parrow</h1>
      <p class="person-role">Director</p>
      <div class="department">
        <p class="department-top">Practitioner Support</p>
        <p class="department-bottom">&amp; Education</p>
      </div>
      <p class="phone">0491 628 403</p>
      <p class="contact-line email">desmond@tualong.net.au</p>
      <p class="contact-line address">218 Kellby St, Kestrel Downs, QLD, 4417</p>
    </div>
  </section>

</body>
</html>
```